Concession stand banners for a mexican food tent

I'm looking for a clean easy to read design for a set of banners I need. More info is on the pic I uploaded. Simple modern design with just text.must say taco,burrito,burrito bowl,salad and nachos. I looking for a dark color(black or brown with colored text. I attached a picture what the setup will look like and where the banners are located.

Target Market(s)

food industry ,food truck, food tent

Font styles to use
Sans Serif

Requirements
Must have
• Must say tacos, burritos, burrito bowls, salads,nachos
Nice to have
• Easy to read from a distance.
Should not have
• hard to read text

```html
<!DOCTYPE html>
<html lang="en">
<head>
<meta charset="utf-8">
<title>Mexican Food Tent – Menu Banner Set</title>
<link rel="stylesheet" href="https://fonts.googleapis.com/css2?family=Bungee&display=swap">
<style>
  :root {
    --page: #e8e6e1;
    --banner: #25233f;
    --banner-edge: #1b1a30;
    --text: #f3eedc;
    --dot-ring: #f7d117;
    --dot-core: #d8281f;
    --stripe-red: #e0261c;
    --stripe-white: #ffffff;
    --trim-yellow: #f4d21a;
  }
  * { box-sizing: border-box; margin: 0; padding: 0; }
  html, body {
    width: 1200px;
    height: 850px;
    overflow: hidden;
    background: var(--page);
  }
  .canvas {
    position: relative;
    width: 1200px;
    height: 850px;
  }
  .banner {
    position: absolute;
    background: var(--banner);
    border: 2px solid var(--banner-edge);
    color: var(--text);
    font-family: "Bungee", sans-serif;
    text-transform: uppercase;
    display: flex;
    flex-direction: column;
    overflow: hidden;
  }
  .banner-body {
    flex: 1;
    display: flex;
    flex-direction: column;
    justify-content: center;
    padding: 0 40px;
  }
  .banner-trim {
    height: 14px;
    background: repeating-linear-gradient(90deg,
      var(--stripe-red) 0 34px,
      var(--stripe-white) 34px 58px);
    border-bottom: 5px solid var(--trim-yellow);
    flex: none;
    height: 19px;
  }
  .menu-line {
    display: flex;
    align-items: center;
    white-space: nowrap;
    letter-spacing: 0.02em;
  }
  .menu-item {
    display: inline-flex;
    align-items: center;
  }
  .bullet {
    display: inline-block;
    width: 0.62em;
    height: 0.62em;
    border-radius: 50%;
    background: radial-gradient(circle, var(--dot-core) 0 34%, var(--dot-ring) 36% 100%);
    margin-right: 0.45em;
    flex: none;
  }

  /* Large stacked banner */
  .banner-main { left: 30px; top: 30px; width: 650px; height: 390px; }
  .banner-main .menu-line { font-size: 46px; line-height: 1.4; }
  .banner-main .menu-item + .menu-item { margin-left: 0.6em; }

  /* Side stacked banner */
  .banner-side { left: 710px; top: 30px; width: 460px; height: 390px; }
  .banner-side .banner-body { padding: 0 34px; }
  .banner-side .menu-line { font-size: 33px; line-height: 1.55; }
  .banner-side .menu-item + .menu-item { margin-left: 0.5em; }

  /* Two-row strip */
  .banner-strip { left: 30px; top: 450px; width: 650px; height: 170px; }
  .banner-strip .banner-body { align-items: center; padding: 0 24px; }
  .banner-strip .menu-line { font-size: 29px; line-height: 1.6; }
  .banner-strip .menu-item + .menu-item { margin-left: 0.75em; }

  /* Three-row counter banner */
  .banner-counter { left: 710px; top: 450px; width: 460px; height: 170px; }
  .banner-counter .banner-body { padding: 0 30px; }
  .banner-counter .menu-line { font-size: 26px; line-height: 1.35; }
  .banner-counter .menu-item + .menu-item { margin-left: 0.6em; }

  /* Wide counter banner */
  .banner-wide { left: 30px; top: 650px; width: 1140px; height: 170px; }
  .banner-wide .banner-body { padding: 0 60px; }
  .banner-wide .menu-grid {
    display: grid;
    grid-template-columns: auto auto auto;
    justify-content: space-between;
    row-gap: 10px;
    font-size: 36px;
  }
  .banner-wide .menu-item { white-space: nowrap; }
</style>
</head>
<body>
<main class="canvas">

  <section class="banner banner-main" aria-label="Menu banner, large">
    <div class="banner-body">
      <p class="menu-line"><span class="menu-item"><span class="bullet"></span>Tacos</span></p>
      <p class="menu-line"><span class="menu-item"><span class="bullet"></span>Burritos</span></p>
      <p class="menu-line"><span class="menu-item"><span class="bullet"></span>Burrito Bowls</span></p>
      <p class="menu-line"><span class="menu-item"><span class="bullet"></span>Salads</span><span class="menu-item"><span class="bullet"></span>Nachos</span></p>
    </div>
    <div class="banner-trim"></div>
  </section>

  <section class="banner banner-side" aria-label="Menu banner, side">
    <div class="banner-body">
      <p class="menu-line"><span class="menu-item"><span class="bullet"></span>Tacos</span></p>
      <p class="menu-line"><span class="menu-item"><span class="bullet"></span>Burritos</span></p>
      <p class="menu-line"><span class="menu-item"><span class="bullet"></span>Burrito Bowls</span></p>
      <p class="menu-line"><span class="menu-item"><span class="bullet"></span>Salads</span><span class="menu-item"><span class="bullet"></span>Nachos</span></p>
    </div>
    <div class="banner-trim"></div>
  </section>

  <section class="banner banner-strip" aria-label="Menu banner, two-row strip">
    <div class="banner-body">
      <p class="menu-line"><span class="menu-item"><span class="bullet"></span>Tacos</span><span class="menu-item"><span class="bullet"></span>Burritos</span><span class="menu-item"><span class="bullet"></span>Salads</span></p>
      <p class="menu-line"><span class="menu-item"><span class="bullet"></span>Burrito Bowls</span><span class="menu-item"><span class="bullet"></span>Nachos</span></p>
    </div>
    <div class="banner-trim"></div>
  </section>

  <section class="banner banner-counter" aria-label="Menu banner, counter right">
    <div class="banner-body">
      <p class="menu-line"><span class="menu-item"><span class="bullet"></span>Tacos</span><span class="menu-item"><span class="bullet"></span>Burritos</span></p>
      <p class="menu-line"><span class="menu-item"><span class="bullet"></span>Burrito Bowls</span></p>
      <p class="menu-line"><span class="menu-item"><span class="bullet"></span>Salads</span><span class="menu-item"><span class="bullet"></span>Nachos</span></p>
    </div>
    <div class="banner-trim"></div>
  </section>

  <section class="banner banner-wide" aria-label="Menu banner, counter front">
    <div class="banner-body">
      <div class="menu-grid">
        <span class="menu-item"><span class="bullet"></span>Tacos</span>
        <span class="menu-item"><span class="bullet"></span>Burritos</span>
        <span class="menu-item"><span class="bullet"></span>Salads</span>
        <span class="menu-item"><span class="bullet"></span>Burrito Bowls</span>
        <span class="menu-item"></span>
        <span class="menu-item"><span class="bullet"></span>Nachos</span>
      </div>
    </div>
    <div class="banner-trim"></div>
  </section>

</main>
</body>
</html>
```